Awesome design needed for standup comedy portal

We need a website designed for a new portal (pebblorx.com) dedicated to standup comedy.

- homepage
- featured "hero" content at top
- banner advertising
- browse comics
- browse venues
- search
- signup / login
- social media links

- comic page
- name
- pictures
- calendar of performances
- list of albums (with buy buttons)
- list of specials (Vodaloom, uCrate, etc. with buy buttons)
- reviews
- latest tweets
- latests photolyn photos
- links to social media accounts
- links to qvrt, podcast

- venue page
- name
- pictures
- address, phone number
- calendar of events
- reviews
- latest tweets
- links to qvrt, podcast

Target Market(s)

Fans of standup comedy and comedians

Number of Pages Required

3 page

Font styles to use
Sans Serif

Requirements
Must have
• Will eventually be implemented in bootstrap, so please keep that in mind

```html
<!DOCTYPE html>
<html lang="en">
<head>
<meta charset="utf-8">
<title>Pebblorx – Standup Comedy Portal</title>
<link href="https://fonts.googleapis.com/css2?family=Roboto:wght@400;500;700;900&display=swap" rel="stylesheet">
<style>
:root{
  --backdrop:#a9cbd9;
  --page:#ffffff;
  --purple:#8a3f8c;
  --purple-light:#a855c9;
  --pink:#d8377e;
  --pink-bright:#f0508f;
  --lavender:#dedbee;
  --lavender-head:#c9c2ee;
  --slate:#62849a;
  --ink:#333;
  --footer:#6d6d6d;
  --side:#e4e1ee;
}
*{box-sizing:border-box;margin:0;padding:0}
html,body{width:871px;height:1200px;overflow:hidden}
body{background:var(--backdrop);font-family:"Roboto",Arial,sans-serif;color:var(--ink);position:relative}
.page{position:absolute;left:79px;top:18px;width:738px;height:1153px;background:var(--page)}
.abs{position:absolute}

/* header */
.site-header{left:0;top:0;width:738px;height:131px;
  background:linear-gradient(90deg,#8a3b3b 0%,#b07a4a 22%,#9aa25a 40%,#6a9a8c 55%,#5aa08a 75%,#4fae8a 100%)}
.header-shade{left:0;top:0;width:738px;height:131px;background:linear-gradient(180deg,rgba(40,40,60,.25),rgba(255,255,255,0) 60%)}
.brand{left:44px;top:74px;display:flex;align-items:center;gap:6px}
.brand-dot{width:22px;height:22px;border-radius:50%;background:#e02b2b}
.brand-name{font-weight:900;font-size:24px;color:#fff;letter-spacing:.5px}
.social-top{right:28px;top:8px;display:flex;gap:7px}
.social-top span{width:20px;height:20px;border-radius:50%;background:var(--pink-bright);display:block}
.cart{right:28px;top:8px;width:22px;height:20px;background:#b05fb8;display:flex;align-items:center;justify-content:center}
.main-nav{left:176px;top:96px;display:flex;gap:6px}
.main-nav a,.account a{display:block;height:23px;line-height:23px;color:#fff;text-decoration:none;font-size:13px;text-align:center;letter-spacing:.5px}
.main-nav a{width:86px;background:rgba(90,160,200,.45)}
.main-nav a.is-active{background:var(--purple-light)}
.account{left:555px;top:96px;display:flex;gap:4px}
.account a{width:76px;background:var(--purple)}

/* search */
.search{left:176px;top:139px;width:449px;height:23px;border:1px solid #bbb;background:#fff}
.search-btn{left:603px;top:139px;width:23px;height:23px;background:var(--purple);display:flex;align-items:center;justify-content:center}

/* calendar */
.calendar{left:25px;top:169px;width:174px;height:198px;background:var(--lavender);box-shadow:0 1px 3px rgba(0,0,0,.25)}
.calendar-title{height:18px;background:var(--lavender-head);color:var(--pink);font-size:10px;text-align:center;line-height:18px}
.calendar-grid{display:grid;grid-template-columns:repeat(7,1fr);padding:6px 6px 0;row-gap:0}
.calendar-grid .dow{font-size:7px;font-weight:500;text-align:center;height:22px;color:#444}
.calendar-grid .day{font-size:8px;font-weight:700;text-align:center;height:26px;color:#222}
.calendar-grid .today span{display:inline-block;width:14px;height:14px;line-height:14px;border-radius:50%;background:#e02b2b;color:#fff;margin-top:-3px}
.calendar-grid .event{color:var(--pink)}

/* hero */
.hero{left:211px;top:168px;width:500px;height:198px;
  background:radial-gradient(circle at 72% 50%,#9fb3e8 0%,#4a6fc6 35%,#2f4fa6 70%,#3a3f9a 100%)}
.hero-arrow{top:72px;color:#d6dcf5;font-size:40px;font-weight:400}
.hero-dots{left:222px;top:176px;display:flex;gap:12px}
.hero-dots span{width:14px;height:14px;border-radius:50%;background:#a9b8e6;border:2px solid #c5d0f0}

/* tags */
.tags-label{left:26px;top:378px;font-size:11px;color:#e02b2b;font-weight:500}
.tags{left:56px;top:372px;display:flex;gap:4px}
.tags span{width:78px;height:24px;line-height:24px;text-align:center;background:var(--purple);color:#fff;font-size:12px;box-shadow:0 2px 2px rgba(0,0,0,.25)}

/* event cards */
.event-card{width:159px}
.event-card .card-head{height:24px;background:var(--slate);color:#fff;font-size:11px;text-align:center;line-height:24px}
.event-card .card-photo{position:relative;height:136px;background:linear-gradient(180deg,#3f6478 0%,#5a7e90 30%,#c95478 52%,#3f6478 70%,#55788a 100%)}
.event-card .card-date{position:absolute;left:0;bottom:0;width:100%;height:24px;background:rgba(110,145,165,.75);color:#fff;font-size:13px;text-align:center;line-height:24px}
.event-card p{font-size:6.6px;line-height:8.5px;color:#555;padding:6px 4px 0;height:48px;text-transform:uppercase}
.event-card .read-more{display:block;text-align:right;font-size:7px;color:var(--pink);padding-right:4px;height:14px}
.event-card .card-actions{display:flex;justify-content:space-between;margin-top:2px}
.event-card .card-actions span{width:76px;height:19px;line-height:19px;text-align:center;background:var(--purple);color:#fff;font-size:10.5px;box-shadow:0 2px 2px rgba(0,0,0,.25)}

/* sidebar */
.sidebar{left:521px;top:416px;width:189px;height:623px;background:var(--side);box-shadow:0 1px 3px rgba(0,0,0,.2)}
.side-title{height:24px;line-height:24px;text-align:center;color:var(--pink);font-size:10px;font-weight:500;background:#f1eff6}
.tweet{display:flex;gap:6px;padding:6px 5px 0;height:51px}
.tweet .avatar{width:42px;height:42px;flex:none;background:linear-gradient(160deg,#8a8f86,#4d5650)}
.tweet h4,.post h4{font-size:9px;color:var(--pink);font-weight:700}
.tweet p,.post p{font-size:6.8px;line-height:8px;color:#666;text-transform:uppercase}
.icons{display:flex;gap:6px;margin-top:2px}
.icons svg{width:9px;height:8px}
.post{padding:8px 5px 0;height:118px}
.post .who{display:flex;align-items:center;gap:5px;margin-bottom:2px}
.post .who i{width:10px;height:10px;border-radius:50%;background:#333;display:block}
.post .shot{height:50px;background:linear-gradient(90deg,#c0653a 0%,#d77a45 50%,#e7a45a 85%,#c9793f 100%);margin-bottom:2px}

/* footer */
.site-footer{left:0;top:1052px;width:738px;height:101px;background:var(--footer);color:#fff}
.address{left:58px;top:18px;font-size:11px;line-height:19.5px}
.address dt{float:left;clear:left;width:38px;font-size:7px;padding-top:2px}
.address dd{margin-left:40px}
.footer-brand{left:340px;top:22px;display:flex;align-items:center;gap:4px}
.footer-brand .brand-dot{width:14px;height:14px}
.footer-brand .brand-name{font-size:14px}
.copyright{left:300px;top:84px;font-size:8px;letter-spacing:.3px}
.social-foot{left:470px;top:21px;display:flex;gap:13px}
.social-foot span{width:40px;height:40px;border-radius:50%;background:var(--pink-bright);color:#fff;font-size:7px;display:flex;align-items:center;justify-content:center;box-shadow:0 2px 3px rgba(0,0,0,.3)}
</style>
</head>
<body>
<div class="page">

  <header class="site-header abs" role="img" aria-label="Blurred multicolour stage lights with a vintage microphone"></header>
  <div class="header-shade abs"></div>
  <div class="brand abs"><span class="brand-dot"></span><span class="brand-name">Pebblorx</span></div>
  <div class="social-top abs" style="right:58px">
    <span title="Photolyn"></span><span title="Chirpa"></span><span title="Facely"></span><span title="Pinora"></span>
  </div>
  <div class="cart abs">
    <svg width="14" height="12" viewBox="0 0 14 12"><path d="M0 1h3l2 7h7l2-5H4" fill="none" stroke="#fff" stroke-width="1.5"/><circle cx="6" cy="10.5" r="1.2" fill="#fff"/><circle cx="11" cy="10.5" r="1.2" fill="#fff"/></svg>
  </div>
  <nav class="main-nav abs">
    <a href="#" class="is-active">HOME</a><a href="#">COMIC</a><a href="#">VENUE</a><a href="#">CONTACT</a>
  </nav>
  <div class="account abs"><a href="#">LOGIN</a><a href="#">SIGNUP</a></div>

  <div class="search abs"></div>
  <div class="search-btn abs">
    <svg width="14" height="14" viewBox="0 0 14 14"><circle cx="6" cy="6" r="4.5" fill="none" stroke="#fff" stroke-width="1.8"/><path d="M9.2 9.2L13 13" stroke="#fff" stroke-width="2"/></svg>
  </div>

  <section class="calendar abs">
    <div class="calendar-title">OCTOBER</div>
    <div class="calendar-grid">
      <div class="dow">MON</div><div class="dow">TUE</div><div class="dow">WED</div><div class="dow">THU</div><div class="dow">FRI</div><div class="dow">SAT</div><div class="dow">SUN</div>
      <div class="day"></div><div class="day"></div><div class="day">1</div><div class="day">2</div><div class="day">3</div><div class="day">4</div><div class="day today"><span>5</span></div>
      <div class="day">6</div><div class="day">7</div><div class="day">8</div><div class="day">9</div><div class="day">10</div><div class="day">11</div><div class="day">12</div>
      <div class="day">13</div><div class="day">14</div><div class="day">15</div><div class="day event">16</div><div class="day">17</div><div class="day">18</div><div class="day">19</div>
      <div class="day">20</div><div class="day">21</div><div class="day">22</div><div class="day">23</div><div class="day">24</div><div class="day">25</div><div class="day">26</div>
      <div class="day">27</div><div class="day">28</div><div class="day">29</div><div class="day">30</div>
    </div>
  </section>

  <section class="hero abs" role="img" aria-label="Chrome stage microphone on a blue gradient background">
    <span class="hero-arrow abs" style="left:6px">&#x27E8;</span>
    <span class="hero-arrow abs" style="right:6px">&#x27E9;</span>
    <div class="hero-dots abs"><span></span><span></span><span></span></div>
  </section>

  <span class="tags-label abs">TAGS</span>
  <div class="tags abs">
    <span>TAG1</span><span>TAG2</span><span>TAG3</span><span>TAG4</span><span>TAG5</span><span>TAG6</span><span>TAG7</span><span>TAG8</span>
  </div>

  <!-- event cards, row 1 -->
  <article class="event-card abs" style="left:23px;top:414px">
    <div class="card-head">MAURIS PORTTITOR</div>
    <div class="card-photo" role="img" aria-label="Rows of red theatre seats"><div class="card-date">25/10/2017</div></div>
    <p>Nulla ex arcu, dictum vitae conva. Lis in, hendrerit elementum orci. Nullam velit arcu, semper sed sectetur quis, rhoncus ac sapien. Aliquam eget felis.</p>
    <span class="read-more">READ MORE</span>
    <div class="card-actions"><span>VENUE</span><span>VENUE 2</span></div>
  </article>
  <article class="event-card abs" style="left:189px;top:416px">
    <div class="card-head">MAURIS PORTTITOR</div>
    <div class="card-photo" role="img" aria-label="Rows of red theatre seats"><div class="card-date">25/10/2017</div></div>
    <p>Nulla ex arcu, dictum vitae conva. Lis in, hendrerit elementum orci. Nullam velit arcu, semper sed sectetur quis, rhoncus ac sapien. Aliquam eget felis.</p>
    <span class="read-more">READ MORE</span>
    <div class="card-actions"><span>VENUE</span><span>VENUE 2</span></div>
  </article>
  <article class="event-card abs" style="left:354px;top:416px">
    <div class="card-head">MAURIS PORTTITOR</div>
    <div class="card-photo" role="img" aria-label="Rows of red theatre seats"><div class="card-date">25/10/2017</div></div>
    <p>Nulla ex arcu, dictum vitae conva. Lis in, hendrerit elementum orci. Nullam velit arcu, semper sed sectetur quis, rhoncus ac sapien. Aliquam eget felis.</p>
    <span class="read-more">READ MORE</span>
    <div class="card-actions"><span>VENUE</span><span>VENUE 2</span></div>
  </article>

  <!-- event cards, row 2 -->
  <article class="event-card abs" style="left:23px;top:684px">
    <div class="card-head">MAURIS PORTTITOR</div>
    <div class="card-photo" role="img" aria-label="Rows of red theatre seats"><div class="card-date">25/10/2017</div></div>
    <p>Nulla ex arcu, dictum vitae conva. Lis in, hendrerit elementum orci. Nullam velit arcu, semper sed sectetur quis, rhoncus ac sapien. Aliquam eget felis.</p>
    <span class="read-more">READ MORE</span>
    <div class="card-actions"><span>VENUE</span><span>VENUE 2</span></div>
  </article>
  <article class="event-card abs" style="left:189px;top:686px">
    <div class="card-head">MAURIS PORTTITOR</div>
    <div class="card-photo" role="img" aria-label="Rows of red theatre seats"><div class="card-date">25/10/2017</div></div>
    <p>Nulla ex arcu, dictum vitae conva. Lis in, hendrerit elementum orci. Nullam velit arcu, semper sed sectetur quis, rhoncus ac sapien. Aliquam eget felis.</p>
    <span class="read-more">READ MORE</span>
    <div class="card-actions"><span>VENUE</span><span>VENUE 2</span></div>
  </article>
  <article class="event-card abs" style="left:354px;top:686px">
    <div class="card-head">MAURIS PORTTITOR</div>
    <div class="card-photo" role="img" aria-label="Rows of red theatre seats"><div class="card-date">25/10/2017</div></div>
    <p>Nulla ex arcu, dictum vitae conva. Lis in, hendrerit elementum orci. Nullam velit arcu, semper sed sectetur quis, rhoncus ac sapien. Aliquam eget felis.</p>
    <span class="read-more">READ MORE</span>
    <div class="card-actions"><span>VENUE</span><span>VENUE 2</span></div>
  </article>

  <aside class="sidebar abs">
    <div class="side-title">CHIRPA</div>
    <div class="tweet"><div class="avatar" role="img" aria-label="Profile photo"></div><div><h4>MAECENAS</h4><p>Phasellus nec ante vitae ante mattis tempus eget nec est.</p>
      <div class="icons"><svg viewBox="0 0 9 8"><path d="M1 3a3 3 0 0 1 6-1M8 5a3 3 0 0 1-6 1" fill="none" stroke="#555" stroke-width="1.2"/></svg><svg viewBox="0 0 9 8"><path d="M1 7c0-3 2-4 6-4M5 1l2 2-2 2" fill="none" stroke="#555" stroke-width="1.2"/></svg><svg viewBox="0 0 9 8"><rect x=".5" y="1" width="8" height="6" fill="#555"/><path d="M.5 1l4 3 4-3" fill="none" stroke="#e4e1ee" stroke-width=".8"/></svg></div></div></div>
    <div class="tweet"><div class="avatar" role="img" aria-label="Profile photo"></div><div><h4>MAECENAS</h4><p>Phasellus nec ante vitae ante mattis tempus eget nec est.</p>
      <div class="icons"><svg viewBox="0 0 9 8"><path d="M1 3a3 3 0 0 1 6-1M8 5a3 3 0 0 1-6 1" fill="none" stroke="#555" stroke-width="1.2"/></svg><svg viewBox="0 0 9 8"><path d="M1 7c0-3 2-4 6-4M5 1l2 2-2 2" fill="none" stroke="#555" stroke-width="1.2"/></svg><svg viewBox="0 0 9 8"><rect x=".5" y="1" width="8" height="6" fill="#555"/><path d="M.5 1l4 3 4-3" fill="none" stroke="#e4e1ee" stroke-width=".8"/></svg></div></div></div>
    <div class="tweet"><div class="avatar" role="img" aria-label="Profile photo"></div><div><h4>MAECENAS</h4><p>Phasellus nec ante vitae ante mattis tempus eget nec est.</p>
      <div class="icons"><svg viewBox="0 0 9 8"><path d="M1 3a3 3 0 0 1 6-1M8 5a3 3 0 0 1-6 1" fill="none" stroke="#555" stroke-width="1.2"/></svg><svg viewBox="0 0 9 8"><path d="M1 7c0-3 2-4 6-4M5 1l2 2-2 2" fill="none" stroke="#555" stroke-width="1.2"/></svg><svg viewBox="0 0 9 8"><rect x=".5" y="1" width="8" height="6" fill="#555"/><path d="M.5 1l4 3 4-3" fill="none" stroke="#e4e1ee" stroke-width=".8"/></svg></div></div></div>
    <div class="tweet"><div class="avatar" role="img" aria-label="Profile photo"></div><div><h4>MAECENAS</h4><p>Phasellus nec ante vitae ante mattis tempus eget nec est.</p>
      <div class="icons"><svg viewBox="0 0 9 8"><path d="M1 3a3 3 0 0 1 6-1M8 5a3 3 0 0 1-6 1" fill="none" stroke="#555" stroke-width="1.2"/></svg><svg viewBox="0 0 9 8"><path d="M1 7c0-3 2-4 6-4M5 1l2 2-2 2" fill="none" stroke="#555" stroke-width="1.2"/></svg><svg viewBox="0 0 9 8"><rect x=".5" y="1" width="8" height="6" fill="#555"/><path d="M.5 1l4 3 4-3" fill="none" stroke="#e4e1ee" stroke-width=".8"/></svg></div></div></div>

    <div class="side-title" style="margin-top:4px;height:30px;line-height:30px">PHOTOLYN</div>
    <div class="post"><div class="who"><i></i><h4>JOHN</h4></div><div class="shot" role="img" aria-label="Golden microphone on an orange background"></div><p>Phasellus nec ante vitae ante mattis tempus eget nec est.</p>
      <div class="icons"><svg viewBox="0 0 9 8"><path d="M4.5 7.5L1 4a2 2 0 0 1 3.5-2.5A2 2 0 0 1 8 4z" fill="#555"/></svg><svg viewBox="0 0 9 8"><path d="M1 3a3 3 0 0 1 6-1M8 5a3 3 0 0 1-6 1" fill="none" stroke="#555" stroke-width="1.2"/></svg><svg viewBox="0 0 9 8"><path d="M1 7c0-3 2-4 6-4M5 1l2 2-2 2" fill="none" stroke="#555" stroke-width="1.2"/></svg><svg viewBox="0 0 9 8"><rect x=".5" y="1" width="8" height="6" fill="#555"/><path d="M.5 1l4 3 4-3" fill="none" stroke="#e4e1ee" stroke-width=".8"/></svg></div></div>
    <div class="post"><div class="who"><i></i><h4>JOHN</h4></div><div class="shot" role="img" aria-label="Golden microphone on an orange background"></div><p>Phasellus nec ante vitae ante mattis tempus eget nec est.</p>
      <div class="icons"><svg viewBox="0 0 9 8"><path d="M4.5 7.5L1 4a2 2 0 0 1 3.5-2.5A2 2 0 0 1 8 4z" fill="#555"/></svg><svg viewBox="0 0 9 8"><path d="M1 3a3 3 0 0 1 6-1M8 5a3 3 0 0 1-6 1" fill="none" stroke="#555" stroke-width="1.2"/></svg><svg viewBox="0 0 9 8"><path d="M1 7c0-3 2-4 6-4M5 1l2 2-2 2" fill="none" stroke="#555" stroke-width="1.2"/></svg><svg viewBox="0 0 9 8"><rect x=".5" y="1" width="8" height="6" fill="#555"/><path d="M.5 1l4 3 4-3" fill="none" stroke="#e4e1ee" stroke-width=".8"/></svg></div></div>
    <div class="post"><div class="who"><i></i><h4>JOHN</h4></div><div class="shot" role="img" aria-label="Golden microphone on an orange background"></div><p>Phasellus nec ante vitae ante mattis tempus eget nec est.</p>
      <div class="icons"><svg viewBox="0 0 9 8"><path d="M4.5 7.5L1 4a2 2 0 0 1 3.5-2.5A2 2 0 0 1 8 4z" fill="#555"/></svg><svg viewBox="0 0 9 8"><path d="M1 3a3 3 0 0 1 6-1M8 5a3 3 0 0 1-6 1" fill="none" stroke="#555" stroke-width="1.2"/></svg><svg viewBox="0 0 9 8"><path d="M1 7c0-3 2-4 6-4M5 1l2 2-2 2" fill="none" stroke="#555" stroke-width="1.2"/></svg><svg viewBox="0 0 9 8"><rect x=".5" y="1" width="8" height="6" fill="#555"/><path d="M.5 1l4 3 4-3" fill="none" stroke="#e4e1ee" stroke-width=".8"/></svg></div></div>
  </aside>

  <footer class="site-footer abs">
    <dl class="address abs">
      <dt>ADDRESS</dt><dd>DORVEL 14 STR.</dd>
      <dt>ZIPCODE</dt><dd>15870</dd>
      <dt>STADE</dt><dd>NEW YORK</dd>
      <dt>PHONE</dt><dd>+30-2105550147</dd>
    </dl>
    <div class="footer-brand abs"><span class="brand-dot"></span><span class="brand-name">Pebblorx</span></div>
    <div class="copyright abs">COPY RIGHT © 2017 PEBBLORX</div>
    <div class="social-foot abs"><span>Photolyn</span><span>Chirpa</span><span>Facely</span><span>Pinora</span></div>
  </footer>

</div>
</body>
</html>
```